Willowbrook Orthodontics needs bag design to promote "Bright Passage"

This SMALL 20cm by 20cm (8 in by 8 in) white canvas bag will be given out to all patients who start their orthodontic treatment with us. Our logo and the bag image are attached. Want to include some sort of our logo/name, and 'established 2011' and 'SMILE MORE, BE HAPPIER' or some other fun/cute sentence. Want this bag to be cute/fun/fashionable.

Target Market(s)

moms, adolescent kids

Industry/Entity Type

dentistry, orthodontics

Colors
0094D4
00A9DD
6FCCEA
C7EBF8
E9F6FB

Requirements
Must have
• (modified )logo/name, simplicity

```html
<!DOCTYPE html>
<html lang="en">
<head>
<meta charset="utf-8">
<title>Willowbrook Orthodontics – Bright Passage tote</title>
<link rel="stylesheet" href="https://fonts.googleapis.com/css2?family=Londrina+Solid:wght@400&family=Jost:wght@300&family=Quicksand:wght@500&display=swap">
<style>
  :root {
    --paper: #ffffff;
    --frame-line: #222222;
    --slogan-blue: #55a9c7;
    --smiley-blue: #93cde1;
    --name-blue: #7cc3da;
    --soft-grey: #a9a9a9;
    --deep-grey: #4f4f4f;
  }
  html, body {
    margin: 0;
    padding: 0;
    overflow: hidden;
  }
  body {
    width: 1200px;
    height: 1060px;
    background: var(--paper);
    position: relative;
  }
  .print-area {
    position: absolute;
    left: 120px;
    top: 50px;
    width: 960px;
    height: 960px;
    box-sizing: border-box;
    border: 1.5px solid var(--frame-line);
    background: var(--paper);
    overflow: hidden;
  }
  .slogan {
    position: absolute;
    left: 0;
    width: 100%;
    margin: 0;
    text-align: center;
    white-space: nowrap;
    font-family: "Londrina Solid", "Arial Narrow", sans-serif;
    font-weight: 400;
    color: var(--slogan-blue);
    line-height: 1;
    letter-spacing: 2px;
  }
  .slogan-text {
    display: inline-block;
    transform-origin: center top;
  }
  .slogan--top {
    top: 78px;
    font-size: 160px;
  }
  .slogan--top .slogan-text {
    transform: scaleX(0.74);
  }
  .slogan--bottom {
    top: 704px;
    font-size: 204px;
  }
  .slogan--bottom .slogan-text {
    transform: scaleX(0.6);
  }
  .brand-dot {
    position: absolute;
    left: 465px;
    top: 335px;
    width: 30px;
    height: 30px;
    border-radius: 50%;
    background: var(--name-blue);
  }
  .brand {
    position: absolute;
    top: 412px;
    left: 0;
    width: 100%;
    text-align: center;
  }
  .brand-name {
    margin: 0;
    font-family: "Jost", "Futura", sans-serif;
    font-weight: 300;
    font-size: 64px;
    color: var(--name-blue);
    letter-spacing: 1px;
    line-height: 1;
    white-space: nowrap;
  }
  .tagline {
    margin: 36px 0 0;
    font-family: "Jost", "Futura", sans-serif;
    font-weight: 300;
    font-size: 44px;
    line-height: 1;
    color: var(--soft-grey);
    letter-spacing: 1.5px;
  }
  .founded {
    margin: 18px 0 0;
    font-family: "Quicksand", sans-serif;
    font-weight: 500;
    font-size: 36px;
    line-height: 1;
    color: var(--deep-grey);
  }
  .smiley {
    position: absolute;
    border-radius: 50%;
    background: var(--smiley-blue);
  }
  .smiley--left  { left: 50px;  top: 619px; width: 133px; height: 133px; }
  .smiley--small { left: 785px; top: 643px; width: 86px;  height: 86px; }
  .smiley--right { left: 804px; top: 748px; width: 136px; height: 136px; }
</style>
</head>
<body>
  <section class="print-area">
    <h1 class="slogan slogan--top"><span class="slogan-text">SMILE MORE</span></h1>

    <span class="brand-dot" aria-hidden="true"></span>
    <div class="brand">
      <p class="brand-name">willowbrook orthodontics</p>
      <p class="tagline">for children and adults</p>
      <p class="founded">established 2011</p>
    </div>

    <div class="smiley smiley--left" role="img" aria-label="Smiley face decoration"></div>
    <div class="smiley smiley--small" role="img" aria-label="Small smiley face decoration"></div>
    <div class="smiley smiley--right" role="img" aria-label="Smiley face decoration"></div>

    <h2 class="slogan slogan--bottom"><span class="slogan-text">BE HAPPIER!</span></h2>
  </section>
</body>
</html>
```